Meridale Legal Letterhead for Law firm must be modern and use the logo I uploaded.

Hello I want a clean modern professional letterhead for my law firm Meridale Legal. A logo has already been created and all files have been uploaded. The information for the firm can be given through message. Please use the logo that has already been created. Please also use the color scheme of that logo. (blue and white).

Target Market(s)

General Public

Industry/Entity Type

Law Firm

Colors

Designer to choose colors to be used in the design.

Requirements
Must have
• This must be a modern professional letterhead
Nice to have
• My logo that is included in file form
Should not have
• Should not have logo that is not the one I uploaded.

```html
<!DOCTYPE html>
<html lang="en">
<head>
<meta charset="utf-8">
<title>Meridale Legal Letterhead</title>
<link href="https://fonts.googleapis.com/css2?family=Lato:wght@400;700&family=Roboto:wght@400&display=swap" rel="stylesheet">
<style>
  :root {
    --backdrop: #e6e6e8;
    --paper: #ffffff;
    --ink: #1a1a1a;
    --header-black: #161616;
    --navy: #2c3166;
    --contact-text: #ffffff;
  }
  * { box-sizing: border-box; margin: 0; padding: 0; }
  html, body {
    width: 1200px; height: 960px; overflow: hidden;
    background: var(--backdrop);
  }
  .letterhead {
    position: absolute; left: 280px; top: 27px;
    width: 640px; height: 905px;
    background: var(--paper);
    font-family: "Lato", sans-serif;
    color: var(--ink);
    box-shadow: 0 2px 10px rgba(0,0,0,0.12);
    overflow: hidden;
  }
  .header-wave { position: absolute; left: 0; top: 0; width: 640px; height: 160px; }
  .contact {
    position: absolute; right: 28px; top: 18px;
    font-family: "Roboto", sans-serif;
    font-size: 7.5px; line-height: 1.4; color: var(--contact-text);
  }
  .contact .address { margin-bottom: 3px; }
  .contact-row { display: flex; align-items: center; gap: 4px; }
  .contact-row svg { width: 6px; height: 6px; flex: none; }
  .firm-mark {
    position: absolute; left: 44px; top: 162px;
    display: flex; align-items: center; gap: 8px;
  }
  .firm-mark .square { width: 12px; height: 12px; background: var(--navy); }
  .firm-mark .name {
    font-size: 11px; font-weight: 400; letter-spacing: 4px;
    text-transform: uppercase; color: var(--navy);
  }
  .letter {
    position: absolute; left: 44px; top: 205px; width: 540px;
    font-size: 9.5px; line-height: 1.4;
  }
  .date { margin-bottom: 14px; font-size: 10px; }
  .recipient { margin-bottom: 12px; font-size: 10px; }
  .salutation { font-weight: 700; font-size: 12.5px; margin: 14px 0 12px; }
  .letter p.body { margin-bottom: 14px; }
  .closing { margin-top: 18px; font-size: 10px; }
  .signature {
    display: block; margin-top: 14px; width: 150px; height: 40px;
    background: linear-gradient(90deg, #ececec, #f6f6f6);
  }
</style>
</head>
<body>
  <article class="letterhead">
    <svg class="header-wave" viewBox="0 0 640 160" aria-hidden="true">
      <path fill="var(--navy)" d="M0,58 C100,92 240,124 400,124 C520,124 590,104 640,92 V104 C590,116 520,136 400,138 C240,140 90,110 0,80 Z"/>
      <path fill="var(--header-black)" stroke="var(--paper)" stroke-width="3" d="M-2,-2 H642 V90 C590,100 520,118 400,118 C240,118 100,88 -2,54 Z"/>
      <path fill="none" stroke="var(--navy)" stroke-width="2" d="M420,146 C520,140 590,122 640,110"/>
    </svg>

    <div class="contact">
      <div class="address">12 Harbour Lane, Brookfield<br>State, Zip 40721</div>
      <div class="contact-row">
        <svg viewBox="0 0 10 10"><path fill="#fff" d="M2 1 L4 1 L5 3.5 L3.8 4.5 C4.4 5.8 5.2 6.6 6.5 7.2 L7.5 6 L10 7 V9 C5 9.5 0.5 5 1 1 Z"/></svg>
        <span>555 018 274</span>
      </div>
      <div class="contact-row">
        <svg viewBox="0 0 10 10"><rect x="0.5" y="2" width="9" height="6.5" fill="#fff"/><path d="M0.5 2 L5 5.5 L9.5 2" stroke="#161616" fill="none"/></svg>
        <span>office@meridalelegal.com</span>
      </div>
      <div class="contact-row">
        <svg viewBox="0 0 10 10"><circle cx="5" cy="5" r="4.5" fill="#fff"/></svg>
        <span>www.meridalelegal.com</span>
      </div>
    </div>

    <div class="firm-mark">
      <span class="square"></span>
      <span class="name">Meridale Legal</span>
    </div>

    <section class="letter">
      <div class="date">January-03-2020</div>
      <div class="recipient">Mr, Arthur Penrose<br>President</div>
      <div class="recipient">Halden Works<br>48 Orchard Row, Suite# 27<br>Brookfield, State, 584117</div>
      <div class="salutation">Dear Mr, Arthur</div>
      <p class="body">Lorem ipsum dolor sit amet, consectetur adipiscing elit, sed do eiusmod tempor incididunt ut labore et dolore magna aliqua. Ut enim ad minim veniam, quis nostrud exercitation ullamco laboris nisi ut aliquip ex ea commodo consequat. Duis aute irure dolor in reprehenderit in voluptate velit esse cillum dolore eu fugiat nulla pariatur.</p>
      <p class="body">Lorem ipsum dolor sit amet, consectetur adipiscing elit, sed do eiusmod tempor incididunt ut labore et dolore magna aliqua. Ut enim ad minim veniam, quis nostrud exercitation ullamco laboris nisi ut aliquip ex ea commodo consequat. Duis aute irure dolor in reprehenderit in voluptate velit esse cillum dolore eu fugiat nulla pariatur.</p>
      <p class="body">Lorem ipsum dolor sit amet, consectetur adipiscing elit, sed do eiusmod tempor incididunt ut labore et dolore magna aliqua. Ut enim ad minim veniam, quis nostrud exercitation ullamco laboris nisi ut aliquip ex ea commodo consequat.</p>
      <p class="body">Excepteur sint occaecat cupidatat non proident, sunt in culpa qui officia deserunt mollit anim id est laborum. re et dolore magnam aliquam quaerat voluptatem.</p>
      <div class="closing">Regards</div>
      <span class="signature" role="img" aria-label="Handwritten signature of Clara Whitfield"></span>
    </section>
  </article>
</body>
</html>
```